Real Estate Sign to Help Modernize and Make it POP!

Design a sign style that would be good for marketing the sale or lease of properties. This will be 3 ' x 4' when printed and needs to look professional, modern, and catchy. It should us the company name, logo, and phone number at a minimum. Keep with the color scheme but open to varieties.

It will be printed and put in a large wooden frame as shown in one of the pictures.

Target Market(s)

Buyers and Tenants

Industry/Entity Type

Real Estate

Requirements
Must have
• company name, logo, and phone number
same color scheme as sign and website
Nice to have
• My Name, "Merrick Halvane, CCIM"
Company Website
Ability to have an easy change from FOR SALE to FOR LEASE or FOR SALE/LEASE when I need to move this sign to a new property
An ability to have reflective colors printed on the contrast for cars to see at night
Should not have
• "Property Managed by"

```html
<!DOCTYPE html>
<html lang="en">
<head>
<meta charset="utf-8">
<title>Meridian Crest Realty – Lease Sign</title>
<link rel="stylesheet" href="https://fonts.googleapis.com/css2?family=Jost:wght@400;500;700&display=swap">
<style>
  :root {
    --page: #8f8f8f;
    --white: #ffffff;
    --navy: #373d49;
    --green: #3e5c55;
    --green-deep: #2c433e;
    --green-soft: #4a6b63;
  }
  * { margin: 0; padding: 0; box-sizing: border-box; }
  html, body {
    width: 954px; height: 1200px; overflow: hidden;
    background: var(--page);
    font-family: "Jost", "Futura", sans-serif;
  }
  .sign {
    position: absolute; left: 27px; top: 0;
    width: 900px; height: 1200px;
    background: var(--white);
    overflow: hidden;
  }
  .headline {
    position: absolute; top: 0; left: 0; width: 100%; height: 212px;
    display: flex; align-items: center; justify-content: center;
    font-weight: 700; font-size: 138px; letter-spacing: 2px;
    color: var(--navy); line-height: 1;
  }
  .hero-shape { position: absolute; left: 0; top: 0; width: 900px; height: 1200px; }
  .brand {
    position: absolute; top: 300px; left: 0; width: 100%;
    display: flex; flex-direction: column; align-items: center; gap: 44px;
  }
  .brand-dot {
    width: 170px; height: 170px; border-radius: 50%;
    background: var(--white);
  }
  .brand-name {
    font-weight: 400; font-size: 64px; letter-spacing: 6px;
    text-transform: uppercase; color: var(--white); line-height: 1;
  }
  .agent-name {
    position: absolute; top: 888px; left: 0; width: 100%;
    text-align: center; font-weight: 400; font-size: 70px;
    color: var(--navy); line-height: 1;
  }
  .agent-phone {
    position: absolute; top: 970px; left: 0; width: 100%;
    display: flex; align-items: center; justify-content: center; gap: 14px;
    font-weight: 700; font-size: 96px; color: var(--green); line-height: 1;
  }
  .agent-phone svg { width: 72px; height: 72px; }
  .web-band {
    position: absolute; left: 0; top: 1081px; width: 100%; height: 119px;
    background: var(--green);
    display: flex; align-items: center; justify-content: center;
    font-weight: 500; font-size: 70px; color: var(--white); line-height: 1;
  }
</style>
</head>
<body>
  <main class="sign">
    <h1 class="headline">FOR LEASE</h1>

    <svg class="hero-shape" viewBox="0 0 900 1200" aria-hidden="false">
      <defs>
        <linearGradient id="heroTone" x1="0" y1="0" x2="0.3" y2="1">
          <stop offset="0" stop-color="#2d4440"/>
          <stop offset="0.6" stop-color="#3a5752"/>
          <stop offset="1" stop-color="#466760"/>
        </linearGradient>
      </defs>
      <polygon role="img" aria-label="Tinted photo of a glass atrium roof seen from below"
               points="0,212 900,212 900,727 450,802 0,727" fill="url(#heroTone)"/>
      <polygon class="chevron" points="0,730 450,822 900,730 900,733 450,852 0,733" fill="var(--navy)"/>
    </svg>

    <div class="brand">
      <div class="brand-dot"></div>
      <div class="brand-name">Meridian Crest Realty</div>
    </div>

    <p class="agent-name">Merrick Halvane, CCIM</p>
    <p class="agent-phone">
      <svg viewBox="0 0 24 24" aria-hidden="true">
        <path fill="var(--green)" d="M6.6 10.8c1.4 2.8 3.8 5.1 6.6 6.6l2.2-2.2c.3-.3.7-.4 1-.2 1.1.4 2.3.6 3.6.6.6 0 1 .4 1 1V20c0 .6-.4 1-1 1C10.6 21 3 13.4 3 4c0-.6.4-1 1-1h3.5c.6 0 1 .4 1 1 0 1.3.2 2.5.6 3.6.1.3 0 .7-.2 1L6.6 10.8z"/>
        <path fill="none" stroke="var(--green)" stroke-width="1.6" stroke-linecap="round" d="M14 6.5a4 4 0 0 1 3.5 3.5M14 3a7.5 7.5 0 0 1 7 7"/>
      </svg>
      985-555-0142
    </p>

    <div class="web-band">meridiancrestrealty.com</div>
  </main>
</body>
</html>
```